Dario Venti Pools , pool construction for residential properties and pool renovations

I have been involved in the pool industry for over 20years and looking to start my own buisnes. My brother and I are teaming up together to make this happen . We will be doing pool renovations to existing old pools "pool makeovers" and also owner builder pools which will save a lot of money in overall cost of a new pool construction. Cards need to be creative not a generic photo of pool ,let's be different.

Target Market(s)

Home owners

Industry/Entity Type

Pool Service

Contact Information for Business Card

Owner builder pools , Pool renovations

Font styles to use
Sans Serif

Colors

Designer to choose colors to be used in the design.

Requirements
Must have
• Mobile number , web , email
Nice to have
• Be creative

```html
<!DOCTYPE html>
<html lang="en">
<head>
<meta charset="utf-8">
<title>Dario Venti Pools – Business Card</title>
<link href="https://fonts.googleapis.com/css2?family=Lato:wght@300;400&display=swap" rel="stylesheet">
<style>
  :root {
    --backdrop: #262626;
    --card-white: #f4f5f5;
    --brand-blue: #2aa8e0;
    --water-light: #5fd0f2;
    --water-mid: #1ea7e4;
    --water-deep: #1a56c8;
    --text-grey: #4a4a4a;
    --icon-blue: #2aa8e0;
    --white: #ffffff;
  }
  html, body {
    margin: 0;
    padding: 0;
    width: 1200px;
    height: 1023px;
    overflow: hidden;
    background: var(--backdrop);
  }
  .canvas {
    position: relative;
    width: 1200px;
    height: 1023px;
  }
  .card {
    position: absolute;
    left: 100px;
    top: 226px;
    width: 1000px;
    height: 571px;
    background: var(--card-white);
    overflow: hidden;
    box-shadow: 0 12px 40px rgba(0,0,0,0.5);
  }
  .card__water {
    position: absolute;
    inset: 0;
    width: 1000px;
    height: 571px;
  }
  .brand {
    position: absolute;
    left: 80px;
    top: 250px;
    margin: 0;
    display: flex;
    align-items: center;
    gap: 14px;
    white-space: nowrap;
    color: var(--brand-blue);
    font-family: "Lato", sans-serif;
    font-weight: 400;
    font-size: 44px;
    line-height: 1;
  }
  .brand__dot {
    width: 16px;
    height: 16px;
    border-radius: 50%;
    background: var(--brand-blue);
    flex: none;
  }
  .contacts {
    position: absolute;
    left: 82px;
    top: 340px;
    margin: 0;
    padding: 0;
    list-style: none;
    font-family: "Lato", sans-serif;
    font-weight: 400;
    font-size: 27px;
    color: var(--text-grey);
  }
  .contacts__item {
    display: flex;
    align-items: center;
    height: 40px;
    white-space: nowrap;
  }
  .contacts__icon {
    width: 22px;
    height: 22px;
    margin-right: 14px;
    flex: none;
  }
  .services {
    position: absolute;
    left: 630px;
    top: 330px;
    margin: 0;
    font-family: "Lato", sans-serif;
    font-weight: 300;
    font-size: 23px;
    letter-spacing: 0.05em;
    color: var(--white);
    line-height: 1.6;
    text-transform: uppercase;
    white-space: nowrap;
  }
</style>
</head>
<body>
<main class="canvas">
  <section class="card">
    <svg class="card__water" viewBox="0 0 1000 571" role="img" aria-label="Photograph of sparkling blue pool water filling the right side of the card">
      <defs>
        <linearGradient id="waterGradient" x1="0" y1="1" x2="1" y2="0">
          <stop offset="0" stop-color="var(--water-light)"/>
          <stop offset="0.45" stop-color="var(--water-mid)"/>
          <stop offset="1" stop-color="var(--water-deep)"/>
        </linearGradient>
      </defs>
      <path d="M560 0 C 640 0, 640 180, 600 260 C 560 340, 470 380, 470 571 L1000 571 L1000 0 Z" fill="url(#waterGradient)"/>
      <path d="M700 0 C 780 0, 780 180, 740 260 C 700 340, 610 380, 610 571 L 540 571 C 540 380, 630 340, 670 260 C 710 180, 710 0, 630 0 Z" fill="rgba(255,255,255,0.16)"/>
    </svg>

    <h1 class="brand"><span class="brand__dot" aria-hidden="true"></span>Dario Venti Pools</h1>

    <ul class="contacts">
      <li class="contacts__item">
        <svg class="contacts__icon" viewBox="0 0 22 22" aria-hidden="true"><rect x="5" y="1.5" width="12" height="19" rx="2" fill="none" stroke="var(--icon-blue)" stroke-width="1.8"/><circle cx="11" cy="17" r="1.1" fill="var(--icon-blue)"/></svg>
        Mobile number
      </li>
      <li class="contacts__item">
        <svg class="contacts__icon" viewBox="0 0 22 22" aria-hidden="true"><rect x="1.5" y="4.5" width="19" height="13" fill="none" stroke="var(--icon-blue)" stroke-width="1.8"/><path d="M1.5 4.5 L11 12 L20.5 4.5 M1.5 17.5 L8.5 10.5 M20.5 17.5 L13.5 10.5" fill="none" stroke="var(--icon-blue)" stroke-width="1.5"/></svg>
        email
      </li>
      <li class="contacts__item">
        <svg class="contacts__icon" viewBox="0 0 22 22" aria-hidden="true"><circle cx="11" cy="11" r="9.5" fill="none" stroke="var(--icon-blue)" stroke-width="1.8"/><ellipse cx="11" cy="11" rx="4" ry="9.5" fill="none" stroke="var(--icon-blue)" stroke-width="1.4"/><path d="M1.5 11 H20.5 M3 6 H19 M3 16 H19" stroke="var(--icon-blue)" stroke-width="1.3"/></svg>
        web
      </li>
    </ul>

    <p class="services">Pool Renovations<br>New Pool Construction</p>
  </section>
</main>
</body>
</html>
```